Front and back cover design for skincare marketing materials

Thank you for showing an interest in my project.
Project Details.

I require a front and back cover for our marketing materials.
·       Front Cover size: 105 mm W x 150 mm H.
·       Back Cover size:  105 mm W x 150 mm H.
·       It must include these two colors. You can use a third color if you wish.
1.     #DBA09D
2.     #FFFFFF
 
Front Cover
·      The front cover will have a faded image of the Kakadu Plum branch and fruit. There are two image files, KP_image-1.jpg and kp_image-2.jpeg. You can use both images, just a portion of them, or source alternative royalty-free images of Kakadu Plum that may better fit the design. These two files have been uploaded.
 
The front cover wording.
Top of the front cover.
a.     The title of the image. “Kakadu Plum”
b.     The brand name, “Velvora Skincare”. The file brand_name.ai uploaded.
 
Bottom of the front cover- Designer's choice of font.
The bottom of the front cover contains three lines of text in the following order.  
1.     Australian Native Ingredients
2.     100% Natural · Organic · Wild-harvested
3.     Australian-Made Premium Skincare
 
Back Cover
·      Back Cover wording.The back cover contains the following words "grown by nature" in white (#FFFFFF) of font Italianno (font_file.ttf) with a background color of #DBA09D as seen in the sample box (sample_box.pdf) right-side panel
 
Please provide one file for the front cover and a separate file for the back cover.
All the elements of the files must be editable.
 
Do NOT use the Curve function on the files, as the text must remain editable/changeable.
 
All assets/resources/files, including fonts not supplied by us but used by the designer, must be named and provided with the finished design.

Target Market(s)

Beauty-minded Asian consumers between the ages of 32 and 75 who take a proactive approach to maintaining younger-looking skin. Those who already know the danger of skin damage caused by skincare containing harsh chemicals choose effective natural/organic solutions to meet their skincare needs. Those who wish a more radiant glow and youthful appearance to their skin. Usually, a two-income middle to high-income bracket couples with a mindset for health and beauty.

Industry/Entity Type

beauty

Font styles to use
Other font styles liked:
• I will provide a font file and a brand name file.

Requirements
Must have
• You must use the two colors provided on the product box. The designer may use a third color.
Nice to have
• some gold colour

```html
<!DOCTYPE html>
<html lang="en">
<head>
<meta charset="utf-8">
<title>Velvora Skincare – Box Panels</title>
<link rel="stylesheet" href="https://fonts.googleapis.com/css2?family=Poppins:wght@400;500&family=Italianno&family=Roboto:wght@700&display=swap">
<style>
  :root {
    --backdrop: #CFD1B2;
    --panel-white: #FFFFFF;
    --brand-pink: #D88DAD;
    --logo-pink: #D99BB6;
    --ink: #111111;
    --leaf-light: #A8C86A;
    --leaf-dark: #3F6B22;
  }
  * { margin: 0; padding: 0; box-sizing: border-box; }
  html, body { width: 1200px; height: 892px; overflow: hidden; }
  body { background: var(--backdrop); position: relative; font-family: "Poppins", sans-serif; color: var(--ink); }

  .sheet-number {
    position: absolute; left: 45px; top: 42px;
    font: 700 41px "Roboto", sans-serif;
  }
  .callout {
    position: absolute;
    font-family: "Roboto", sans-serif; font-weight: 700; line-height: 1.05;
  }
  .callout--top { left: 171px; top: 347px; font-size: 30px; line-height: 1.25; }
  .callout--front { left: 158px; top: 570px; font-size: 52px; line-height: 1.25; }
  .callout--back { left: 856px; top: 570px; font-size: 52px; }
  .arrows { position: absolute; left: 0; top: 0; }

  .panel { position: absolute; }
  .panel--top-fold {
    left: 326px; top: 73px; width: 253px; height: 376px;
    background: var(--panel-white);
    border-radius: 126px 126px 0 0;
  }
  .panel--front {
    left: 326px; top: 449px; width: 252px; height: 362px;
    background: var(--panel-white);
    text-align: center;
  }
  .panel--back {
    left: 578px; top: 449px; width: 253px; height: 362px;
    background: var(--brand-pink);
  }

  .brand-name {
    position: absolute; left: 0; width: 100%; text-align: center;
    font-family: "Poppins", sans-serif; font-weight: 400;
    color: var(--logo-pink); font-size: 22px; letter-spacing: 0.5px;
  }
  .panel--top-fold .brand-name { top: 230px; }
  .panel--front .brand-name { top: 92px; }

  .product-title {
    position: absolute; left: 0; width: 100%; top: 35px;
    font-size: 29px; font-weight: 400; line-height: 1;
  }
  .product-photo {
    position: absolute; left: 60px; top: 169px; width: 132px; height: 89px;
    background: linear-gradient(135deg, var(--leaf-light), var(--leaf-dark) 70%, #6FA0D0);
  }
  .product-claims {
    position: absolute; left: 0; width: 100%; top: 278px;
    font-size: 10px; font-weight: 500; line-height: 15px;
  }
  .tagline {
    position: absolute; left: 50%; top: 50%;
    transform: translate(-50%, -50%) rotate(-90deg);
    white-space: nowrap;
    font-family: "Italianno", cursive; font-size: 60px;
    color: var(--panel-white); line-height: 1;
  }
</style>
</head>
<body>
  <div class="sheet-number">N0.1</div>

  <svg class="arrows" width="1200" height="892" viewBox="0 0 1200 892" aria-hidden="true">
    <g fill="none" stroke="#111" stroke-width="4">
      <polyline points="222,344 222,282 282,282"/>
      <polyline points="222,569 222,508 282,508"/>
      <polyline points="931,568 931,508 873,508"/>
    </g>
    <g fill="#111">
      <polygon points="294,282 279,274 279,290"/>
      <polygon points="294,508 279,500 279,516"/>
      <polygon points="861,508 876,500 876,516"/>
    </g>
  </svg>

  <div class="callout callout--top">Top<br>Folding</div>
  <div class="callout callout--front">Front<br>Side</div>
  <div class="callout callout--back">Back Side</div>

  <section class="panel panel--top-fold">
    <div class="brand-name">Velvora Skincare</div>
  </section>

  <section class="panel panel--front">
    <h1 class="product-title">Kakadu Plum</h1>
    <div class="brand-name">Velvora Skincare</div>
    <div class="product-photo" role="img" aria-label="Kakadu plum branch with green fruit and leaves"></div>
    <p class="product-claims">
      Australian Native Ingredients<br>
      100% Natural · Organic · Wild-harvested<br>
      Australian-Made Premium Skincare
    </p>
  </section>

  <section class="panel panel--back">
    <p class="tagline">grown by nature</p>
  </section>
</body>
</html>
```